Zelvrin
business cards & stationery
Project: Zelvrin
Zelvrin -
Creative Brief
Simple
Marcus Holt
VP Sales & Marketing
417 Fenwick Ave. #615-284 Brookmere Falls, NV 89733
temporary@zelvrin-example.com
www.zelvrin-example.com
Your Game, Everywhere

```html
<!DOCTYPE html>
<html lang="en">
<head>
<meta charset="utf-8">
<title>Zelvrin – Business Card</title>
<link rel="stylesheet" href="https://fonts.googleapis.com/css2?family=Questrial&display=swap">
<style>
  :root {
    --sky-top: #6cbcee;
    --sky-mid: #b9defa;
    --sky-low: #eef7fd;
    --band: #050608;
    --band-edge: #ffffff;
    --wordmark: #2b3038;
    --accent: #2f8fe6;
    --text-light: #ffffff;
    --text-muted: #c9ced6;
  }
  html, body {
    margin: 0;
    padding: 0;
    width: 1200px;
    height: 686px;
    overflow: hidden;
    background: #ffffff;
  }
  .card {
    position: relative;
    width: 1200px;
    height: 686px;
    overflow: hidden;
    background: linear-gradient(180deg, var(--sky-top) 0%, var(--sky-mid) 45%, var(--sky-low) 75%);
    font-family: "Questrial", sans-serif;
  }
  .card-shapes {
    position: absolute;
    inset: 0;
  }
  .brand {
    position: absolute;
    left: 0;
    right: 0;
    top: 120px;
    display: flex;
    justify-content: center;
    align-items: center;
    gap: 34px;
  }
  .brand-name {
    font-size: 168px;
    line-height: 1;
    letter-spacing: 10px;
    text-transform: uppercase;
    color: var(--wordmark);
  }
  .brand-dot {
    width: 92px;
    height: 92px;
    border-radius: 50%;
    background: var(--accent);
  }
  .person {
    position: absolute;
    left: 0;
    right: 0;
    top: 510px;
    text-align: center;
    color: var(--text-light);
  }
  .person-name {
    margin: 0;
    font-size: 54px;
    font-weight: 400;
    font-variant: small-caps;
    letter-spacing: 5px;
    line-height: 1;
  }
  .person-title {
    margin: 8px 0 0;
    font-size: 28px;
    letter-spacing: 3px;
    color: var(--text-muted);
  }
  .contact {
    position: absolute;
    bottom: 28px;
    margin: 0;
    font-size: 22px;
    line-height: 46px;
    color: var(--text-light);
    font-style: normal;
  }
  .contact-online { left: 24px; }
  .contact-address { right: 28px; text-align: left; }
</style>
</head>
<body>
  <main class="card">
    <svg class="card-shapes" width="1200" height="686" viewBox="0 0 1200 686" aria-hidden="true">
      <path class="band-edge" d="M0,530 Q600,420 1200,530" fill="none" stroke="var(--band-edge)" stroke-width="10" opacity="0.9"/>
      <path class="band" d="M0,540 Q600,432 1200,540 L1200,686 L0,686 Z" fill="var(--band)"/>
    </svg>

    <div class="brand">
      <span class="brand-name">Zelvrin</span>
      <span class="brand-dot"></span>
    </div>

    <section class="person">
      <h1 class="person-name">Marcus Holt</h1>
      <p class="person-title">VP Sales &amp; Marketing</p>
    </section>

    <address class="contact contact-online">
      Email: temporary@zelvrin-example.com<br>
      Website: www.zelvrin-example.com
    </address>

    <address class="contact contact-address">
      417 Fenwick Ave. #615-284<br>
      Brookmere Falls, NV 89733
    </address>
  </main>
</body>
</html>
```